Business Card Design - Pediatric Dentist

We need a business card for a new dental office. We are a pediatric dentist in Austin Tx. I would like a design that use bright green and if possible light blue.

Target Market(s)

Marketed to young moms

Industry/Entity Type

Dental

Contact Information for Business Card

Marcus Hollin DDS
Tidewell Pediatric Dentistry
438 E. Corvell Lane. Austin TX 78731
(512) 284 9153.

In the back i would like to state "we take most insurances, Chip & Medicaid" & a map

Colors
add136
cadf82
85cae6

```html
<!DOCTYPE html>
<html lang="en">
<head>
<meta charset="utf-8">
<title>Tidewell Pediatric Dentistry – Business Card</title>
<link rel="stylesheet" href="https://fonts.googleapis.com/css2?family=Tinos&display=swap">
<style>
  :root {
    --page: #ffffff;
    --lime: #a6ff00;
    --sky: #8ef2f2;
    --pale-lime: #c6ff66;
    --grass: #3cff12;
    --mark-green: #40e03a;
    --ink: #000000;
    --edge: #ffffff;
  }
  html, body {
    margin: 0;
    width: 1200px;
    height: 1000px;
    overflow: hidden;
    background: var(--page);
  }
  .card {
    position: absolute;
    left: 56px;
    top: 181px;
    width: 1085px;
    height: 635px;
    background: var(--lime);
    overflow: hidden;
    font-family: "Tinos", "Times New Roman", serif;
    color: var(--ink);
  }
  .card-art {
    position: absolute;
    inset: 0;
  }
  .brand-dot {
    position: absolute;
    left: 85px;
    top: 80px;
    width: 210px;
    height: 210px;
    border-radius: 50%;
    background: var(--mark-green);
  }
  .brand-name {
    position: absolute;
    left: 347px;
    top: 78px;
    margin: 0;
    font-weight: 400;
    font-size: 70px;
    line-height: 79px;
    letter-spacing: 0.5px;
  }
  .contact {
    position: absolute;
    right: 46px;
    top: 376px;
    margin: 0;
    font-style: normal;
    text-align: right;
    font-size: 34px;
    line-height: 45px;
  }
</style>
</head>
<body>
  <div class="card">
    <svg class="card-art" width="1085" height="635" viewBox="56 181 1085 635" aria-hidden="true">
      <g class="waves" fill="none" stroke-width="21">
        <path stroke="var(--sky)" d="M40,668 C200,664 260,712 340,710 C430,708 470,662 660,666"/>
        <path stroke="var(--pale-lime)" d="M40,688 C200,684 260,732 340,730 C430,728 470,682 660,686"/>
        <path stroke="var(--grass)" d="M40,708 C200,704 260,752 340,750 C430,748 470,702 660,706"/>
      </g>
      <polygon class="contact-star" fill="var(--sky)" stroke="var(--edge)" stroke-width="3"
        points="916,336 1056,538 1170,564 1170,830 697,830 700,768 538,598 768,548"/>
    </svg>

    <div class="brand-dot"></div>
    <h1 class="brand-name">Tidewell<br>Pediatric<br>Dentistry</h1>

    <address class="contact">
      Marcus Hollin, DDS<br>
      Tidewell Pediatric Dentistry<br>
      438 E. Corvell Lane<br>
      Austin, TX 78731<br>
      (512) 284-9153
    </address>
  </div>
</body>
</html>
```